Veltrium stationery design

Design stationery for us that fits with the colours of the logo. We are looking for letterheads, business cards etc. Something we can use for a prospectus and marketing presentations in power point. Must be completed in such a manner that it represents a corporate image for large enterprise clients and other large organisations. The company is a project assurance and monitoring company that works in all industries.

```html
<!DOCTYPE html>
<html lang="en">
<head>
<meta charset="utf-8">
<title>Veltrium Envelope Stationery</title>
<link rel="stylesheet" href="https://fonts.googleapis.com/css2?family=Montserrat:wght@400;800&display=swap">
<style>
  :root {
    --navy: #0f2a55;
    --navy-deep: #0b2149;
    --orange: #f5650f;
    --white: #ffffff;
    --paper-shade: #eef0f3;
    --backdrop: #4b4c4e;
  }
  html, body {
    margin: 0;
    padding: 0;
    width: 1200px;
    height: 1200px;
    overflow: hidden;
    background: var(--backdrop);
    font-family: "Montserrat", Arial, sans-serif;
  }
  .canvas {
    position: relative;
    width: 1200px;
    height: 1200px;
  }
  .envelope {
    position: absolute;
    left: 100px;
    width: 1000px;
    height: 460px;
    box-shadow: 0 14px 30px rgba(0,0,0,0.35);
    overflow: hidden;
  }
  /* Front face */
  .envelope--front {
    top: 90px;
    background: var(--white);
  }
  .front__band {
    position: absolute;
    left: 0;
    top: 0;
    width: 22px;
    height: 100%;
    background: var(--orange);
  }
  .front__flap {
    position: absolute;
    right: 0;
    top: 0;
    width: 190px;
    height: 100%;
  }
  .brand {
    position: absolute;
    left: 300px;
    top: 200px;
    display: flex;
    align-items: center;
    gap: 16px;
  }
  .brand__dot {
    width: 40px;
    height: 40px;
    border-radius: 50%;
    background: var(--orange);
  }
  .brand__name {
    font-weight: 800;
    font-size: 54px;
    letter-spacing: 2px;
    color: var(--navy);
  }
  /* Back face */
  .envelope--back {
    top: 650px;
    background: var(--navy);
  }
  .contact {
    position: absolute;
    left: 50px;
    top: 60px;
    margin: 0;
    padding: 0;
    list-style: none;
    color: var(--white);
    font-size: 22px;
    font-weight: 400;
  }
  .contact__item {
    display: flex;
    align-items: center;
    gap: 12px;
    margin-bottom: 10px;
  }
  .contact__icon {
    width: 20px;
    height: 20px;
    flex: none;
  }
  .address-window {
    position: absolute;
    right: 70px;
    bottom: 50px;
    width: 330px;
    height: 130px;
    background: var(--white);
    border-radius: 10px;
    box-shadow: inset 0 2px 6px rgba(0,0,0,0.25);
  }
</style>
</head>
<body>
<main class="canvas">

  <section class="envelope envelope--front" aria-label="Envelope front">
    <div class="front__band"></div>
    <svg class="front__flap" viewBox="0 0 190 460" preserveAspectRatio="none" aria-hidden="true">
      <polygon points="40,0 190,0 190,460 40,460 0,420 0,40" fill="var(--navy-deep)"/>
    </svg>
    <div class="brand">
      <span class="brand__dot"></span>
      <span class="brand__name">VELTRIUM</span>
    </div>
  </section>

  <section class="envelope envelope--back" aria-label="Envelope back">
    <ul class="contact">
      <li class="contact__item">
        <svg class="contact__icon" viewBox="0 0 24 24" aria-hidden="true">
          <path d="M6.6 10.8a15 15 0 0 0 6.6 6.6l2.2-2.2c.3-.3.7-.4 1-.2 1.1.4 2.3.6 3.6.6.6 0 1 .4 1 1V20c0 .6-.4 1-1 1A17 17 0 0 1 3 4c0-.6.4-1 1-1h3.5c.6 0 1 .4 1 1 0 1.3.2 2.5.6 3.6.1.3 0 .7-.2 1z" fill="var(--orange)"/>
        </svg>
        <span>(000) 000 0000</span>
      </li>
      <li class="contact__item">
        <svg class="contact__icon" viewBox="0 0 24 24" aria-hidden="true">
          <rect x="2" y="5" width="20" height="14" rx="1" fill="var(--orange)"/>
          <path d="M2 6l10 7 10-7" fill="none" stroke="var(--navy)" stroke-width="1.8"/>
        </svg>
        <span>email@company.com</span>
      </li>
      <li class="contact__item">
        <svg class="contact__icon" viewBox="0 0 24 24" aria-hidden="true">
          <circle cx="12" cy="12" r="10" fill="var(--orange)"/>
          <path d="M2 12h20M12 2c3 3 3 17 0 20M12 2c-3 3-3 17 0 20" fill="none" stroke="var(--navy)" stroke-width="1.5"/>
        </svg>
        <span>www.company.com</span>
      </li>
    </ul>
    <div class="address-window"></div>
  </section>

</main>
</body>
</html>
```